Bref créative
MOBILE ULTRASOUND BUSINESS
Professional
Nora K. Pellway Hussel
President and Director of Ultrasound
517 Thornbury Lane #2614
Millbrook Twp. PA. 15832
nora@keystonepulsescanworks.example
keystonepulsescanworks.example
We need business cards for my husband as well, all info will be the same except for his name is Gavin P. Hussel - Chief Operating Officer for title - and gavin@keystonepulsescanworks.example
vector logo file

```html
<!DOCTYPE html>
<html lang="en">
<head>
<meta charset="utf-8">
<title>Mobile Ultrasound Business Cards</title>
<link rel="stylesheet" href="https://fonts.googleapis.com/css2?family=Arimo:wght@400;700&display=swap">
<style>
  :root {
    --stage: #1b1b1b;
    --card: #060708;
    --card-edge: #2a2d30;
    --name-blue: #29a6e6;
    --brand-blue: #2b9fe0;
    --body-text: #d7e3b0;
    --title-text: #e8ecef;
    --band-dark: #0a4f86;
    --band-light: #35b3f0;
    --rule: #5a6066;
  }
  * { box-sizing: border-box; margin: 0; padding: 0; }
  html, body { width: 1200px; height: 871px; overflow: hidden; }
  body {
    background: var(--stage);
    font-family: "Arimo", Arial, sans-serif;
    position: relative;
  }
  .card {
    position: absolute;
    left: 384px;
    width: 410px;
    height: 226px;
    background: var(--card);
    border: 1px solid var(--card-edge);
    border-radius: 12px;
    overflow: hidden;
  }
  .card--president { top: 80px; }
  .card--coo { top: 334px; }
  .card--back { top: 588px; }

  .brand {
    position: absolute;
    left: 26px;
    top: 96px;
    display: flex;
    align-items: center;
    gap: 8px;
  }
  .card--back .brand { left: 128px; top: 100px; }
  .brand__mark { width: 18px; height: 18px; background: var(--brand-blue); }
  .brand__name {
    color: var(--brand-blue);
    font-weight: 700;
    font-size: 17px;
    letter-spacing: 1px;
  }

  .person {
    position: absolute;
    right: 20px;
    top: 18px;
    text-align: right;
  }
  .person__name { color: var(--name-blue); font-weight: 700; font-size: 14px; }
  .person__title { color: var(--title-text); font-size: 8px; margin-top: 4px; }

  .contact {
    position: absolute;
    right: 14px;
    top: 70px;
    list-style: none;
    text-align: right;
  }
  .card--coo .contact { top: 68px; }
  .contact li {
    color: var(--body-text);
    font-size: 6.5px;
    line-height: 9.5px;
    display: flex;
    justify-content: flex-end;
    align-items: center;
    gap: 10px;
  }
  .contact li.gap { margin-top: 5px; }
  .contact svg { width: 7px; height: 7px; flex: none; }
  .contact .no-icon { padding-right: 17px; }

  .divider {
    position: absolute;
    left: 185px;
    width: 1px;
    background: var(--rule);
  }
  .card--president .divider { top: 72px; height: 100px; }
  .card--coo .divider { top: 70px; height: 100px; }

  .band {
    position: absolute;
    left: 0;
    right: 0;
    height: 14px;
    background: linear-gradient(90deg, var(--band-dark), var(--band-light) 55%, var(--band-dark));
  }
  .band::before {
    content: "";
    position: absolute;
    left: 0; right: 0; top: -5px;
    height: 2px;
    background: linear-gradient(90deg, #222, #8a9096 50%, #222);
  }
  .card--president .band, .card--coo .band { top: 190px; }
</style>
</head>
<body>

<article class="card card--president">
  <div class="person">
    <p class="person__name">Nora K. Pellway Hussel</p>
    <p class="person__title">President and Director of Ultrasound</p>
  </div>
  <div class="brand"><span class="brand__mark"></span><span class="brand__name">BRQMOLVEX</span></div>
  <div class="divider"></div>
  <ul class="contact">
    <li class="no-icon">517 Thornbury Lane #2614</li>
    <li>Millbrook Twp. PA. 15832 <svg viewBox="0 0 10 10"><path d="M5 0.5a3.2 3.2 0 0 1 3.2 3.2C8.2 6.2 5 9.5 5 9.5S1.8 6.2 1.8 3.7A3.2 3.2 0 0 1 5 0.5z" fill="#d7e3b0"/></svg></li>
    <li class="gap">412 555 0187 <svg viewBox="0 0 10 10"><path d="M2 1l2 2-1 1.2c.6 1.2 1.6 2.2 2.8 2.8L7 6l2 2-1.3 1.3C4.5 9 1 5.5.7 2.3z" fill="#d7e3b0"/></svg></li>
    <li>(888) 555-0142 <svg viewBox="0 0 10 10"><rect x="1" y="2" width="8" height="6" fill="#d7e3b0"/></svg></li>
    <li class="gap">nora@keystonepulsescanworks.example <svg viewBox="0 0 10 10"><rect x="0.5" y="2" width="9" height="6" fill="none" stroke="#d7e3b0"/><path d="M0.5 2l4.5 3.5L9.5 2" fill="none" stroke="#d7e3b0"/></svg></li>
    <li>keystonepulsescanworks.example <svg viewBox="0 0 10 10"><circle cx="5" cy="5" r="4" fill="none" stroke="#d7e3b0"/><path d="M1 5h8M5 1v8" stroke="#d7e3b0"/></svg></li>
    <li class="gap">Keystone_Pulse_Scan_Works <svg viewBox="0 0 10 10"><circle cx="5" cy="5" r="4" fill="#d7e3b0"/></svg></li>
  </ul>
  <div class="band"></div>
</article>

<article class="card card--coo">
  <div class="person">
    <p class="person__name">Gavin P. Hussel</p>
    <p class="person__title">Chief Operating Officer</p>
  </div>
  <div class="brand"><span class="brand__mark"></span><span class="brand__name">BRQMOLVEX</span></div>
  <div class="divider"></div>
  <ul class="contact">
    <li class="no-icon">517 Thornbury Lane #2614</li>
    <li>Millbrook Twp. PA. 15832 <svg viewBox="0 0 10 10"><path d="M5 0.5a3.2 3.2 0 0 1 3.2 3.2C8.2 6.2 5 9.5 5 9.5S1.8 6.2 1.8 3.7A3.2 3.2 0 0 1 5 0.5z" fill="#d7e3b0"/></svg></li>
    <li class="gap">412 555 0187 <svg viewBox="0 0 10 10"><path d="M2 1l2 2-1 1.2c.6 1.2 1.6 2.2 2.8 2.8L7 6l2 2-1.3 1.3C4.5 9 1 5.5.7 2.3z" fill="#d7e3b0"/></svg></li>
    <li>(888) 555-0142 <svg viewBox="0 0 10 10"><rect x="1" y="2" width="8" height="6" fill="#d7e3b0"/></svg></li>
    <li class="gap">gavin@keystonepulsescanworks.example <svg viewBox="0 0 10 10"><rect x="0.5" y="2" width="9" height="6" fill="none" stroke="#d7e3b0"/><path d="M0.5 2l4.5 3.5L9.5 2" fill="none" stroke="#d7e3b0"/></svg></li>
    <li>keystonepulsescanworks.example <svg viewBox="0 0 10 10"><circle cx="5" cy="5" r="4" fill="none" stroke="#d7e3b0"/><path d="M1 5h8M5 1v8" stroke="#d7e3b0"/></svg></li>
    <li class="gap">Keystone_Pulse_Scan_Works <svg viewBox="0 0 10 10"><circle cx="5" cy="5" r="4" fill="#d7e3b0"/></svg></li>
  </ul>
  <div class="band"></div>
</article>

<article class="card card--back">
  <div class="brand"><span class="brand__mark"></span><span class="brand__name">BRQMOLVEX</span></div>
</article>

</body>
</html>
```